Website redesign for a Cloud Advisory business

We are looking to revisit our existing brand and website, with a view to updating both. Looking for concepts and designs for how the website might look, flow and feel. Current website is: www.brightlane.com.au

Scope and Deliverables: Concept design for the home page and one internal page.

We do not expect you to design all the pages and all the elements of the website at this stage.

This job is not for the full website design, but just for concepts that we can start with when we go into the full website design.

We would love to see a design feature based on our name, logo, or industry, which can run through banners and other collateral (chirpnet banner, ads on Findora, corporate documents etc).

We want the brand to properly depict what we bring/deliver to businesses when consulting to them and this should extend to the colour scheme, logo, font (perhaps updated) and copy (which will be supplied).

Our brand should suitably communicate our ability, knowledge and extensive experience within the Cloud space.

It should express and evoke credibility, knowledge and understanding of the Cloud space, independence, gravitas, reliability, efficiency, trust, expertise, approachability, service delivery but be uncomplicated, practical and use plain speaking language.

Colours that reinforce this might include: Blues, blacks, silver, white, grey and our existing orange.

Website designs that we like or have referenced include:

Skyvault: http://skyvault.com.au/ - This has good information but looks a little amateur in it’s cartoon like design and colour scheme. Also, this seems to be aimed at clients more interested in price than design and what we are going for is a little more high end.

Nimbuspath: https://www.nimbuspath.com.au/ - This site has merit in its’ setup but little call to action on the home page, especially before the scroll line. I like the set up of the Case Studies page however I’d look to make it more prominent by having it set up 3 across rather than the 4 they have. Something such as this: https://www.tallyrig.com/case-studies

Pelwyn: http://www.pelwyn.com.au/#home4 - This page is a good one as far as selling services and information on the company. I quite like it.

BorealIT: http://www.borealit.com.au/ - While I don’t think is particularly creative, it does practically depict the services we offer in a fairly clear way and might be a bit of a basic (albeit dull) template to follow.

QRV: https://store.qrv.com/us/Product-Family/QRV-Advisory-Services/QRV-Cloud-Advisory-Service/p/QRV-Services-Cloud-Advisory - This offers substantial information but is probably a little confusing although the roll-over drop down menus have merit.

LUP: http://www.lup.net.au/en/services/ - While this in not quite what we are looking for, the colour scheme gives it more gravitas and quality.

As another reference, this website and the way they present their case studies is also something we like, although I’d like them shown 3 up, side by side…. https://www.tallyrig.com/case-studies.

We have added a page layout and page purpose document.

Target Market(s)

Corporates, small - medium business, direct referrals, via search results

Industry/Entity Type

Business

Number of Pages Required

1 page

Font styles to use
Sans Serif

Colors
85abd2
0455a3
000000
f37122
5c5c5c

Requirements
Must have
• Website must be mobile device compatible.
• Concept design for the home page.
Nice to have
• We would love to see a design feature based on our name, logo, or industry, which can run through banners and other collateral (chirpnet banner, ads on Findora, corporate documents etc).

```html
<!DOCTYPE html>
<html lang="en">
<head>
<meta charset="utf-8">
<title>Brightlane – Impartial Cloud Solutions</title>
<link href="https://fonts.googleapis.com/css2?family=Ubuntu:wght@400;500&family=Roboto:wght@500;700&display=swap" rel="stylesheet">
<style>
:root{
  --blue:#0455a3;
  --sky:#85abd2;
  --orange:#f37122;
  --ink:#1e1e1e;
  --grey:#5c5c5c;
  --mist:#d6d6d6;
  --pale:#eeeef2;
  --white:#ffffff;
}
*{box-sizing:border-box;margin:0;padding:0}
html,body{width:1200px;height:3058px;overflow:hidden}
body{font-family:'Ubuntu',sans-serif;color:var(--ink);background:var(--white);position:relative}
.abs{position:absolute}
.btn-orange{background:var(--orange);color:var(--white);font-size:20px;border-radius:3px;display:flex;align-items:center;justify-content:center;border:1px solid #e0601a}
.topbar{top:0;left:0;width:1200px;height:76px;background:var(--blue)}
.topbar .btn-orange{left:894px;top:15px;width:269px;height:52px}
.header{top:76px;left:0;width:1200px;height:164px;background:var(--white);box-shadow:0 3px 4px rgba(0,0,0,.25)}
.brand{left:37px;top:41px;display:flex;align-items:center;gap:14px}
.brand-mark{width:64px;height:64px;background:var(--orange)}
.brand-name{font-size:52px;font-weight:500;color:var(--ink);letter-spacing:1px}
.menu{left:1110px;top:68px;width:47px}
.menu span{display:block;height:5px;background:var(--grey);margin-bottom:8px;border-radius:2px}
.hero{top:243px;left:0;width:1200px;height:525px;background:linear-gradient(90deg,#6e7073 0%,#707275 55%,#4a4b4e 80%,#2a2a2c 100%)}
.hero h1{position:absolute;top:118px;width:100%;text-align:center;font-family:'Ubuntu',sans-serif;font-weight:500;font-size:60px;color:var(--white)}
.section-title{font-family:'Roboto',sans-serif;font-weight:700;font-size:22px;color:#2b2b2b;position:absolute;left:70px}
.rule{position:absolute;left:70px;width:938px;height:2px;background:#8a8a8a}
.about{top:768px;left:0;width:1200px;height:316px;background:var(--sky)}
.about p{position:absolute;left:70px;top:120px;width:980px;font-size:23px;line-height:34px;color:#222}
.btn-ghost{position:absolute;left:70px;top:211px;width:254px;height:49px;border:2px solid #3e4a57;color:#2b2b2b;font-size:21px;display:flex;align-items:center;justify-content:center;border-radius:2px}
.solutions{top:1084px;left:0;width:1200px;height:665px;background:var(--white)}
.card{position:absolute;top:142px;width:353px;height:457px}
.card .photo{position:absolute;left:0;top:0;width:353px;height:399px}
.card .icon{position:absolute;left:32px;top:34px}
.card .kicker{position:absolute;left:36px;top:210px;font-size:28px;color:var(--white)}
.card .name{position:absolute;left:36px;top:248px;font-size:40px;color:var(--white);letter-spacing:1px}
.card .blurb{position:absolute;left:36px;top:316px;width:300px;font-size:19px;line-height:24px;color:var(--white);white-space:nowrap;overflow:hidden;text-overflow:ellipsis}
.card .blurb span{display:block;overflow:hidden;text-overflow:ellipsis}
.card .more{position:absolute;left:0;top:399px;width:353px;height:58px;background:var(--orange);color:var(--white);font-size:23px;display:flex;align-items:center;padding-left:36px;gap:12px}
.testimonials{top:1749px;left:0;width:1200px;height:498px;background:var(--mist)}
.avatar{position:absolute;left:484px;top:119px;width:140px;height:140px;border-radius:50%;background:radial-gradient(circle,#9a9a9a,#505050);border:3px solid #f2f2f2}
.quote{position:absolute;left:150px;top:295px;width:900px;text-align:center;font-size:20px;line-height:37px;color:#333}
.dots{position:absolute;top:448px;left:514px;display:flex;gap:11px}
.dots i{width:12px;height:12px;border-radius:50%;border:1.5px solid #888;display:block}
.dots i.on{background:#444;border-color:#444}
.clients{top:2247px;left:0;width:1200px;height:600px;background:var(--pale)}
.logo-tile{position:absolute;width:292px;height:163px;background:var(--white);border:1px solid #b5b5b5;display:flex;align-items:center;justify-content:center;font-size:44px;font-weight:500;color:#3a3a3a}
.footer{top:2847px;left:0;width:1200px;height:142px;background:var(--blue)}
.footer .btn-orange{position:absolute;left:464px;top:44px;width:271px;height:53px}
.legal{top:2989px;left:0;width:1200px;height:69px;background:var(--grey)}
.legal p{position:absolute;left:30px;top:23px;font-size:17px;color:var(--white)}
.social{position:absolute;top:12px;width:44px;height:44px;border-radius:50%;color:var(--white);font-size:14px;display:flex;align-items:center;justify-content:center}
</style>
</head>
<body>

<div class="abs topbar"><div class="abs btn-orange">Book a free consultation</div></div>

<header class="abs header">
  <div class="abs brand"><div class="brand-mark"></div><div class="brand-name">BRIGHTLANE</div></div>
  <div class="abs menu"><span></span><span></span><span></span></div>
</header>

<section class="abs hero" role="img" aria-label="Hand touching a row of device icons beside a cloud">
  <h1>Impartial Cloud Solutions</h1>
</section>

<section class="abs about">
  <h2 class="section-title" style="top:45px">ABOUT US</h2>
  <div class="rule" style="top:85px"></div>
  <p>We help you pick the right add-on solution for your business. Personalised solution design, set-up, conversion, training and support for you.</p>
  <div class="btn-ghost">Learn more about us</div>
</section>

<section class="abs solutions">
  <h2 class="section-title" style="top:44px">SOLUTIONS</h2>
  <div class="rule" style="top:83px"></div>

  <div class="card" style="left:60px">
    <div class="photo" role="img" aria-label="Snowy mountain peaks under cloud" style="background:linear-gradient(180deg,#5d7d96 0%,#8a9fb2 45%,#607385 100%)"></div>
    <svg class="icon" width="130" height="120" viewBox="0 0 130 120" fill="none" stroke="#fff" stroke-width="4"><path d="M30 78a22 22 0 0 1 4-43 30 30 0 0 1 58-4 24 24 0 0 1 8 47z"/><rect x="22" y="62" width="70" height="46"/><line x1="10" y1="112" x2="110" y2="112"/></svg>
    <div class="kicker">Cloud</div>
    <div class="name">ADVISORY</div>
    <div class="blurb"><span>Find the right systems for you.</span><span>Devise a cloud strategy.</span></div>
    <div class="more">Read More <svg width="14" height="22" viewBox="0 0 14 22"><path d="M3 3l8 8-8 8" stroke="#fff" stroke-width="3" fill="none"/></svg></div>
  </div>

  <div class="card" style="left:423px">
    <div class="photo" role="img" aria-label="Consultants meeting at an office desk" style="background:linear-gradient(160deg,#9aa2a8 0%,#767e84 50%,#4f565b 100%)"></div>
    <svg class="icon" width="170" height="120" viewBox="0 0 170 120" fill="none" stroke="#fff" stroke-width="4"><ellipse cx="60" cy="52" rx="56" ry="40"/><path d="M30 86l-10 22 30-18"/><circle cx="88" cy="46" r="30" fill="#fff"/><path d="M88 30v32M72 46h32" stroke="#555" stroke-width="8"/></svg>
    <div class="kicker">Solutions</div>
    <div class="name">CONSULTING</div>
    <div class="blurb"><span>We provide impartial advice on</span><span>solutions ensuring it's always…</span></div>
    <div class="more">Read More <svg width="14" height="22" viewBox="0 0 14 22"><path d="M3 3l8 8-8 8" stroke="#fff" stroke-width="3" fill="none"/></svg></div>
  </div>

  <div class="card" style="left:787px">
    <div class="photo" role="img" aria-label="Hands joining puzzle pieces" style="background:linear-gradient(160deg,#7d93a6 0%,#5f7a90 50%,#4a6277 100%)"></div>
    <svg class="icon" width="150" height="110" viewBox="0 0 150 110" fill="none" stroke="#fff" stroke-width="4"><ellipse cx="75" cy="12" rx="22" ry="7" fill="#fff"/><rect x="53" y="12" width="44" height="34" fill="#fff"/><path d="M75 46v14M20 60h110M20 60v12M75 60v12M130 60v12"/><rect x="6" y="72" width="28" height="20"/><rect x="61" y="72" width="28" height="20"/><rect x="116" y="72" width="28" height="20"/></svg>
    <div class="kicker">Systems</div>
    <div class="name">INTEGRATION</div>
    <div class="blurb"><span>Automate repetitive tasks,</span><span>connect your in-house applica…</span></div>
    <div class="more">Read More <svg width="14" height="22" viewBox="0 0 14 22"><path d="M3 3l8 8-8 8" stroke="#fff" stroke-width="3" fill="none"/></svg></div>
  </div>
</section>

<section class="abs testimonials">
  <h2 class="section-title" style="top:50px">TESTIMONIALS</h2>
  <div class="rule" style="top:88px"></div>
  <div class="avatar" role="img" aria-label="Portrait of client Dorian Falke"></div>
  <p class="quote">"I am very pleased with your service. You were particularly good to work with, very sympathetic, and quick to reply. We gained a great deal of confidence working with you and have streamlined our accounting in ledgerly." - Dorian Falke</p>
  <div class="dots"><i class="on"></i><i></i><i></i><i></i><i></i></div>
</section>

<section class="abs clients">
  <h2 class="section-title" style="top:53px">SOME OF OUR CLIENTS</h2>
  <div class="rule" style="top:90px"></div>
  <div class="logo-tile" style="left:149px;top:161px">Hollen</div>
  <div class="logo-tile" style="left:454px;top:161px">Marrowby</div>
  <div class="logo-tile" style="left:759px;top:161px">Tillco</div>
  <div class="logo-tile" style="left:149px;top:337px">Jobnook</div>
  <div class="logo-tile" style="left:454px;top:337px">Quarro</div>
  <div class="logo-tile" style="left:759px;top:337px">Ostrava Group</div>
</section>

<footer class="abs footer"><div class="btn-orange">Book a free consultation</div></footer>

<div class="abs legal">
  <p>Copyright 2015 Brightlane. All rights reserved.</p>
  <div class="social" style="left:993px;background:#3b5a9a" aria-label="Friendbook">Fb</div>
  <div class="social" style="left:1056px;background:#2a9fd8" aria-label="chirpnet">Ch</div>
  <div class="social" style="left:1118px;background:#d84a32" aria-label="Findora">Fi</div>
</div>

</body>
</html>
```